Pet store web design

I would like to redesign my current online store (http://brindlecove.example)
I'm looking for a clean, modern design. Any ideas are welcome..

Industry/Entity Type

Pet

Number of Pages Required

3 page

```html
<!DOCTYPE html>
<html lang="en">
<head>
<meta charset="utf-8">
<title>Brindle Cove – Pet Store</title>
<link rel="stylesheet" href="https://fonts.googleapis.com/css2?family=Open+Sans:wght@300;400;600;700&display=swap">
<style>
:root{
  --yellow:#f4c20d;
  --yellow-dark:#e0ad00;
  --nav:#3b3b3b;
  --teal:#1a9d9f;
  --teal-dark:#14807f;
  --page:#eeeeee;
  --white:#ffffff;
  --ink:#333333;
  --muted:#8a8a8a;
  --sale:#e53935;
  --footer:#202020;
  --footer-bottom:#151515;
  --blue:#1e6fc4;
}
*{box-sizing:border-box;margin:0;padding:0}
html,body{width:1200px;height:2252px;overflow:hidden}
body{font-family:"Open Sans",Arial,sans-serif;background:var(--page);color:var(--ink);font-size:13px;position:relative}
.wrap{width:1040px;margin:0 auto;position:relative}

/* header */
.header{background:var(--yellow);height:152px}
.topbar{height:26px;display:flex;justify-content:center;gap:34px;font-size:11px;color:#5b4a00;align-items:center;padding-top:4px}
.topbar span{display:flex;align-items:center;gap:5px}
.topbar i{width:8px;height:8px;background:#7a6300;border-radius:2px;display:inline-block}
.header-main{display:flex;justify-content:space-between;align-items:flex-start;padding-top:10px}
.brand{display:flex;align-items:center;gap:10px;font-weight:700;font-size:30px;color:#3b3b3b}
.brand-dot{width:34px;height:34px;border-radius:50%;background:#3b3b3b}
.header-tools{display:flex;flex-direction:column;align-items:flex-end;gap:8px;padding-top:14px}
.cart{display:flex;align-items:center;gap:10px;font-weight:600;font-size:14px;color:#3b3b3b}
.search{width:210px;height:26px;background:var(--white);border-radius:2px;display:flex;align-items:center;justify-content:space-between;padding:0 8px;font-size:11px;color:var(--muted)}
.nav{background:var(--nav);height:32px}
.nav ul{list-style:none;display:flex;gap:40px;height:32px;align-items:center}
.nav li{color:var(--white);font-weight:700;font-size:12px;letter-spacing:.5px}

/* hero */
.hero{display:flex;gap:20px;margin-top:44px}
.hero-main{width:700px;height:352px;background:var(--white);position:relative;display:flex;align-items:center;padding-left:40px}
.hero-text h1{font-weight:400;font-size:58px;color:var(--teal);letter-spacing:2px;line-height:1}
.hero-text p{font-size:13px;color:var(--muted);margin:10px 0 10px;letter-spacing:1px}
.hero-text h2{font-weight:400;font-size:34px;color:#4a4a4a}
.hero-photo{position:absolute;right:30px;top:40px;width:370px;height:270px;background:linear-gradient(135deg,#cbbfae,#8d7c6a 60%,#5a4c40)}
.dots{position:absolute;bottom:14px;left:50%;display:flex;gap:6px}
.dots i{width:8px;height:8px;border-radius:50%;background:#ccc}
.dots i:first-child{background:var(--teal)}
.hero-side{display:flex;flex-direction:column;gap:22px;width:320px}
.promo{background:var(--white);height:165px;display:flex;justify-content:space-between;padding:18px}
.promo-photo{width:120px;height:120px}
.promo h3{font-size:17px;font-weight:600;color:#3b3b3b;line-height:1.2}
.promo p{font-size:10px;color:var(--muted);margin-top:6px;line-height:1.4}
.promo .more{margin-top:10px;color:#555;font-weight:700;letter-spacing:2px}

/* tabs */
.tabs{display:flex;justify-content:center;gap:46px;margin-top:78px;font-weight:700;font-size:15px;color:#333}
.tabs .active{color:var(--teal);border-bottom:2px solid var(--teal);padding-bottom:4px}

/* products */
.grid{display:grid;grid-template-columns:repeat(4,240px);column-gap:26px;row-gap:40px;margin-top:38px}
.card{background:var(--white);height:330px;position:relative;display:flex;flex-direction:column}
.sale{position:absolute;right:14px;top:12px;color:var(--sale);font-size:11px;font-weight:700}
.card-photo{height:150px;margin:28px auto 14px;width:120px}
.price{padding:0 16px;font-size:14px;font-weight:700;display:flex;gap:8px}
.price s{color:var(--muted);font-weight:400}
.price em{font-style:normal;color:var(--teal);margin-left:auto}
.card h4{padding:4px 16px 0;font-size:12px;font-weight:600}
.card .desc{padding:2px 16px 0;font-size:10px;color:var(--muted)}
.card-foot{margin-top:auto;border-top:1px solid #e6e6e6;height:44px;display:flex;align-items:center}
.card-foot .add{width:56px;display:flex;justify-content:center;border-right:1px solid #e6e6e6;height:100%;align-items:center}
.card-foot .more{flex:1;text-align:center;color:var(--teal);font-weight:700;font-size:14px}

/* info */
.info{display:grid;grid-template-columns:500px 500px;gap:40px;margin-top:72px;row-gap:40px}
.info-item{display:flex;height:144px}
.info-photo{width:152px;height:144px}
.info-body{flex:1;background:var(--teal);color:var(--white);padding:18px 18px 0 22px;position:relative}
.info-body h3{font-size:23px;font-weight:600;line-height:1.1}
.info-body p{font-size:10px;margin-top:8px;line-height:1.45;opacity:.9;width:200px}
.read{position:absolute;right:16px;bottom:14px;display:flex;align-items:center;gap:8px;font-size:11px;font-weight:700}
.read i{width:20px;height:20px;border-radius:50%;background:#0f6d6d;display:flex;align-items:center;justify-content:center}

/* footer */
.footer{position:absolute;left:0;top:1920px;width:1200px;height:332px;background:var(--footer);color:#cfcfcf}
.footer-inner{display:flex;padding-top:32px;gap:0}
.subscribe{width:340px}
.subscribe h3{color:var(--white);font-weight:400;font-size:18px;letter-spacing:1px}
.subscribe .field{width:240px;height:30px;background:var(--white);margin-top:14px}
.subscribe .btn{width:90px;height:28px;background:var(--blue);color:var(--white);font-size:11px;font-weight:700;display:flex;align-items:center;justify-content:center;margin-top:12px}
.cards{display:flex;gap:8px;margin-top:28px}
.cards i{width:44px;height:28px;background:#d9d9d9;border-radius:3px}
.cols{display:flex;gap:0;flex:1}
.col{width:175px}
.col h4{color:var(--white);font-size:13px;font-weight:700;margin-bottom:14px}
.col li{list-style:none;font-size:11px;line-height:2;color:#bdbdbd}
.social{display:flex;gap:8px;margin-top:54px}
.social i{width:22px;height:22px;border-radius:2px}
.footer-bottom{position:absolute;bottom:0;left:0;width:100%;height:34px;background:var(--footer-bottom);font-size:10px;color:#9a9a9a}
.footer-bottom .wrap{line-height:34px}
</style>
</head>
<body>

<header class="header">
  <div class="topbar">
    <span><i></i>My Account</span>
    <span><i></i>Login</span>
    <span><i></i>My Wishlist</span>
    <span><i></i>Checkout</span>
  </div>
  <div class="wrap header-main">
    <div class="brand"><span class="brand-dot"></span>Brindle Cove</div>
    <div class="header-tools">
      <div class="cart">
        <svg width="22" height="18" viewBox="0 0 22 18"><path d="M1 2h4l3 10h10l3-7H7" fill="none" stroke="#3b3b3b" stroke-width="2"/><circle cx="9" cy="16" r="1.6" fill="#3b3b3b"/><circle cx="17" cy="16" r="1.6" fill="#3b3b3b"/></svg>
        0 (800) 555 0142
      </div>
      <div class="search">Search entire store here
        <svg width="12" height="12" viewBox="0 0 12 12"><circle cx="5" cy="5" r="3.8" fill="none" stroke="#888" stroke-width="1.5"/><path d="M8 8l3 3" stroke="#888" stroke-width="1.5"/></svg>
      </div>
    </div>
  </div>
</header>

<nav class="nav">
  <ul class="wrap"><li>DOG</li><li>CAT</li><li>FISH</li><li>BIRD</li><li>SMALL PET</li></ul>
</nav>

<main class="wrap">
  <section class="hero">
    <div class="hero-main">
      <div class="hero-text">
        <h1>SALE</h1>
        <p>MAURIS SODALES, MAGNA VITAE</p>
        <h2>UPTO 50 % OFF</h2>
      </div>
      <div class="hero-photo" role="img" aria-label="Two cats resting together"></div>
      <div class="dots"><i></i><i></i><i></i></div>
    </div>
    <div class="hero-side">
      <div class="promo">
        <div class="promo-photo" role="img" aria-label="Cat house with a cat inside" style="background:linear-gradient(135deg,#d8d2c8,#8e8a84)"></div>
        <div style="width:150px">
          <h3>Dog / Cat House</h3>
          <p>Sed pulvinar vel lectus nec porta congue</p>
          <div class="more">•••</div>
        </div>
      </div>
      <div class="promo">
        <div style="width:150px">
          <h3>Dog Clothing &amp; Accessories</h3>
          <p>Sed pulvinar vel lectus nec porta congue</p>
          <div class="more">•••</div>
        </div>
        <div class="promo-photo" role="img" aria-label="Two small dogs in clothing" style="background:linear-gradient(135deg,#efe6d6,#c2a27a)"></div>
      </div>
    </div>
  </section>

  <div class="tabs">
    <span class="active">POPULAR</span><span>NEW ARRIVALS</span><span>BEST SELLERS</span><span>SPECIALS</span>
  </div>

  <section class="grid">
    <article class="card"><span class="sale">Sale!</span><div class="card-photo" role="img" aria-label="Dog in a grey costume" style="background:linear-gradient(#e8e8ec,#b9bcc6)"></div><div class="price">$30.69 <s>$45.25</s><em>20 %</em></div><h4>Chef Dog Costume - Large</h4><p class="desc">Nunc pulvinar dui vitae urna</p><div class="card-foot"><span class="add"><svg width="18" height="15" viewBox="0 0 22 18"><path d="M1 2h4l3 10h10l3-7H7" fill="none" stroke="#555" stroke-width="2"/><circle cx="9" cy="16" r="1.6" fill="#555"/><circle cx="17" cy="16" r="1.6" fill="#555"/></svg></span><span class="more">More</span></div></article>
    <article class="card"><span class="sale">Sale!</span><div class="card-photo" role="img" aria-label="Dog in a green coat" style="background:linear-gradient(#e3f1d6,#7cbf3c)"></div><div class="price">$30.69 <s>$45.25</s><em>20 %</em></div><h4>Chef Dog Costume - Large</h4><p class="desc">Nunc pulvinar dui vitae urna</p><div class="card-foot"><span class="add"><svg width="18" height="15" viewBox="0 0 22 18"><path d="M1 2h4l3 10h10l3-7H7" fill="none" stroke="#555" stroke-width="2"/><circle cx="9" cy="16" r="1.6" fill="#555"/><circle cx="17" cy="16" r="1.6" fill="#555"/></svg></span><span class="more">More</span></div></article>
    <article class="card"><span class="sale">Sale!</span><div class="card-photo" role="img" aria-label="Round olive pet bed" style="background:linear-gradient(#e6e8cc,#9aa04a)"></div><div class="price">$30.69 <s>$45.25</s><em>20 %</em></div><h4>Chef Dog Costume - Large</h4><p class="desc">Nunc pulvinar dui vitae urna</p><div class="card-foot"><span class="add"><svg width="18" height="15" viewBox="0 0 22 18"><path d="M1 2h4l3 10h10l3-7H7" fill="none" stroke="#555" stroke-width="2"/><circle cx="9" cy="16" r="1.6" fill="#555"/><circle cx="17" cy="16" r="1.6" fill="#555"/></svg></span><span class="more">More</span></div></article>
    <article class="card"><span class="sale">Sale!</span><div class="card-photo" role="img" aria-label="Red pet treadmill" style="background:linear-gradient(#f1d6d6,#c7262c)"></div><div class="price">$30.69 <s>$45.25</s><em>20 %</em></div><h4>Chef Dog Costume - Large</h4><p class="desc">Nunc pulvinar dui vitae urna</p><div class="card-foot"><span class="add"><svg width="18" height="15" viewBox="0 0 22 18"><path d="M1 2h4l3 10h10l3-7H7" fill="none" stroke="#555" stroke-width="2"/><circle cx="9" cy="16" r="1.6" fill="#555"/><circle cx="17" cy="16" r="1.6" fill="#555"/></svg></span><span class="more">More</span></div></article>
    <article class="card"><span class="sale">Sale!</span><div class="card-photo" role="img" aria-label="Beige cat scratching tower" style="background:linear-gradient(#ece4d6,#b8a888)"></div><div class="price">$30.69 <s>$45.25</s><em>20 %</em></div><h4>Chef Dog Costume - Large</h4><p class="desc">Nunc pulvinar dui vitae urna</p><div class="card-foot"><span class="add"><svg width="18" height="15" viewBox="0 0 22 18"><path d="M1 2h4l3 10h10l3-7H7" fill="none" stroke="#555" stroke-width="2"/><circle cx="9" cy="16" r="1.6" fill="#555"/><circle cx="17" cy="16" r="1.6" fill="#555"/></svg></span><span class="more">More</span></div></article>
    <article class="card"><span class="sale">Sale!</span><div class="card-photo" role="img" aria-label="Red pet treadmill" style="background:linear-gradient(#f1d6d6,#c7262c)"></div><div class="price">$30.69 <s>$45.25</s><em>20 %</em></div><h4>Chef Dog Costume - Large</h4><p class="desc">Nunc pulvinar dui vitae urna</p><div class="card-foot"><span class="add"><svg width="18" height="15" viewBox="0 0 22 18"><path d="M1 2h4l3 10h10l3-7H7" fill="none" stroke="#555" stroke-width="2"/><circle cx="9" cy="16" r="1.6" fill="#555"/><circle cx="17" cy="16" r="1.6" fill="#555"/></svg></span><span class="more">More</span></div></article>
    <article class="card"><span class="sale">Sale!</span><div class="card-photo" role="img" aria-label="Dog in a green coat" style="background:linear-gradient(#e3f1d6,#7cbf3c)"></div><div class="price">$30.69 <s>$45.25</s><em>20 %</em></div><h4>Chef Dog Costume - Large</h4><p class="desc">Nunc pulvinar dui vitae urna</p><div class="card-foot"><span class="add"><svg width="18" height="15" viewBox="0 0 22 18"><path d="M1 2h4l3 10h10l3-7H7" fill="none" stroke="#555" stroke-width="2"/><circle cx="9" cy="16" r="1.6" fill="#555"/><circle cx="17" cy="16" r="1.6" fill="#555"/></svg></span><span class="more">More</span></div></article>
    <article class="card"><span class="sale">Sale!</span><div class="card-photo" role="img" aria-label="Dog in a grey costume" style="background:linear-gradient(#e8e8ec,#b9bcc6)"></div><div class="price">$30.69 <s>$45.25</s><em>20 %</em></div><h4>Chef Dog Costume - Large</h4><p class="desc">Nunc pulvinar dui vitae urna</p><div class="card-foot"><span class="add"><svg width="18" height="15" viewBox="0 0 22 18"><path d="M1 2h4l3 10h10l3-7H7" fill="none" stroke="#555" stroke-width="2"/><circle cx="9" cy="16" r="1.6" fill="#555"/><circle cx="17" cy="16" r="1.6" fill="#555"/></svg></span><span class="more">More</span></div></article>
  </section>

  <section class="info">
    <div class="info-item"><div class="info-photo" role="img" aria-label="Delivery courier with a parcel" style="background:linear-gradient(135deg,#f3eee4,#c9b48e)"></div><div class="info-body"><h3>Delivery<br>Information</h3><p>Ut rhoncus urna quam, a rutrum nunc aliquet eget felis.</p><span class="read">Read More <i><svg width="8" height="8" viewBox="0 0 8 8"><path d="M2 1l3 3-3 3" fill="none" stroke="#fff" stroke-width="1.5"/></svg></i></span></div></div>
    <div class="info-item"><div class="info-photo" role="img" aria-label="Question mark sign" style="background:linear-gradient(135deg,#d6d6d6,#5a5a5a)"></div><div class="info-body"><h3>Recent<br>FAQ's</h3><p>Ut rhoncus urna quam, a rutrum nunc aliquet eget felis.</p><span class="read">Read More <i><svg width="8" height="8" viewBox="0 0 8 8"><path d="M2 1l3 3-3 3" fill="none" stroke="#fff" stroke-width="1.5"/></svg></i></span></div></div>
    <div class="info-item"><div class="info-photo" role="img" aria-label="Returns and refunds road sign" style="background:linear-gradient(135deg,#3c5f9c,#1e2f55)"></div><div class="info-body"><h3>Returns &amp;<br>Query</h3><p>Ut rhoncus urna quam, a rutrum nunc aliquet eget felis.</p><span class="read">Read More <i><svg width="8" height="8" viewBox="0 0 8 8"><path d="M2 1l3 3-3 3" fill="none" stroke="#fff" stroke-width="1.5"/></svg></i></span></div></div>
    <div class="info-item"><div class="info-photo" role="img" aria-label="Customer support agent" style="background:linear-gradient(135deg,#f1e6dc,#b88a6a)"></div><div class="info-body"><h3>Get<br>Our Help</h3><p>Ut rhoncus urna quam, a rutrum nunc aliquet eget felis.</p><span class="read">Read More <i><svg width="8" height="8" viewBox="0 0 8 8"><path d="M2 1l3 3-3 3" fill="none" stroke="#fff" stroke-width="1.5"/></svg></i></span></div></div>
  </section>
</main>

<footer class="footer">
  <div class="wrap footer-inner">
    <div class="subscribe">
      <h3>SUBSCRIBE</h3>
      <div class="field"></div>
      <div class="btn">SUBMIT</div>
      <div class="cards"><i></i><i></i></div>
    </div>
    <div class="cols">
      <div class="col"><h4>Shop Now</h4><ul><li>Dog</li><li>Cat</li><li>Fish</li><li>Bird</li><li>Pet Rats</li><li>Small Animal</li></ul></div>
      <div class="col"><h4>Services</h4><ul><li>Pet Grooming</li><li>Pet Magazine</li><li>Gift Bag Make</li><li>Pet Grave</li><li>Puppy School</li></ul></div>
      <div class="col"><h4>Shiping Online</h4><ul><li>Delivery Information</li><li>Privacy Policy</li><li>Returns Policy</li><li>Terms and Conditions</li><li>FAQs</li></ul></div>
      <div class="col"><h4>Info</h4><ul><li>About Us</li><li>Contact Us</li><li>Our Blog</li><li>Contact us</li></ul>
        <div class="social"><i style="background:#3b5998"></i><i style="background:#d23a2c"></i><i style="background:#c8232c"></i><i style="background:#1da1f2"></i></div>
      </div>
    </div>
  </div>
  <div class="footer-bottom"><div class="wrap">©2025 BRINDLE COVE. © 2025 | PRIVACY POLICY</div></div>
</footer>

</body>
</html>
```